Pilates and Boxing group Fitness business needs a promotional postcard.

One sided postcard only please!
We are a new fitness business by the name of 'The Willow Loft'.
We need a promotional postcard to advertise our business and the classes that are available. The call to action for this promotion is 'Your first class is FREE!
We provide pilates mat classes with the use of props such as balls, foam rollers, stretch bands and most importantly - a barre (ballet). Our classes aim to achieve improvement in strength, flexibility and better posture.
We also provide a cardio class called boxing barre that consists of upper and lower body boxing choreography with balance and lower body strength work on the barre. This class is to the latest upbeat music.
I have included a few photos that can be used as well as our logo. I am happy for other suggestions.
The following must be on the postcard:
1. Logo
2. Pilates and Boxing classes that move your body and soul!
3. Pilates mat classes
4. Boxing Barre Classes
5. website: www.thewillowloft.com.au
6. email: info@thewillowloft.com.au
7. Ph: 0498367205
8. Your first class is free! (PLEASE MAKE EYE CATCHING!)
9. BOOK Online - limited spaces!
10. Address: Unit 7 of 12 Pemberly Rd, Ashgrove Vale 2163
Please make it eye catching and I do not want it cluttered. Our colours are electric blue and black (shown in the logo). I am happy for other colours as well.
Our tagline is "Breathe. Balance. Flow" - so I want the advertisement to communicate peace and joy in movement.
Target Market(s)
The demographic is to adults of both genders.
Industry/Entity Type
Fitness
Look and feel
Each slider illustrates characteristics of the customer's brand and the style your logo design should communicate.

```html
<!DOCTYPE html>
<html lang="en">
<head>
<meta charset="utf-8">
<title>The Willow Loft – Postcard</title>
<link href="https://fonts.googleapis.com/css2?family=Open+Sans:ital,wght@0,400;0,600;1,400&display=swap" rel="stylesheet">
<style>
  :root {
    --backdrop: #000000;
    --card: #ffffff;
    --electric-blue: #1f4fa8;
    --teal: #2dbfa6;
    --ink: #111111;
    --skin-light: #e9cdb8;
    --skin-mid: #c99a80;
    --hair: #6b4a34;
  }
  * { margin: 0; padding: 0; box-sizing: border-box; }
  html, body {
    width: 1200px; height: 1025px; overflow: hidden;
    background: var(--backdrop);
    font-family: "Open Sans", Arial, sans-serif;
  }
  .postcard {
    position: absolute; left: 72px; top: 172px;
    width: 1056px; height: 683px;
    background: var(--card); overflow: hidden;
  }
  .hero-photo {
    position: absolute; left: 0; top: 0; width: 640px; height: 683px;
    background:
      linear-gradient(90deg, rgba(255,255,255,0) 0%, rgba(255,255,255,0) 60%, var(--card) 100%),
      radial-gradient(ellipse 45% 40% at 40% 38%, var(--skin-light) 0%, var(--skin-mid) 60%, transparent 100%),
      linear-gradient(180deg, var(--hair) 0%, var(--skin-mid) 35%, var(--skin-light) 65%, #4b4f55 100%);
  }
  .brand {
    position: absolute; left: 636px; top: 46px; width: 400px;
  }
  .brand-name {
    display: flex; align-items: center; gap: 14px;
    font-size: 46px; font-weight: 400; color: var(--electric-blue); line-height: 1.1;
  }
  .brand-mark {
    width: 22px; height: 22px; border-radius: 50%; background: var(--electric-blue); flex: none;
  }
  .brand-tagline {
    margin-top: 20px; font-size: 19px; font-style: italic; color: var(--electric-blue);
  }
  .headline {
    position: absolute; right: 32px; top: 198px; text-align: right;
    font-size: 38px; line-height: 54px; color: var(--teal); font-weight: 400;
  }
  .class-list {
    position: absolute; left: 632px; top: 340px; list-style: none;
    font-size: 31px; line-height: 44px; color: var(--electric-blue);
  }
  .offer {
    position: absolute; right: 32px; top: 464px;
    font-size: 46px; line-height: 56px; color: var(--electric-blue); font-weight: 400;
  }
  .booking-band {
    position: absolute; left: 0; top: 572px; width: 460px; height: 42px;
  }
  .booking-band svg { position: absolute; inset: 0; }
  .booking-band span {
    position: relative; display: block; padding-left: 18px;
    font-size: 26px; line-height: 42px; color: #fff;
  }
  .contact {
    position: absolute; right: 36px; top: 564px; text-align: right;
    font-size: 19px; line-height: 25px; color: var(--electric-blue); font-style: normal;
  }
  .contact .phone { margin-right: 14px; }
  .website {
    position: absolute; right: 20px; top: 642px;
    font-size: 19px; color: var(--ink);
  }
</style>
</head>
<body>
  <main class="postcard">
    <div class="hero-photo" role="img" aria-label="Photo of a woman in a boxing stance, fists raised toward the camera"></div>

    <header class="brand">
      <div class="brand-name"><span class="brand-mark"></span>The Willow Loft</div>
      <p class="brand-tagline">Breathe. Balance. Flow</p>
    </header>

    <h1 class="headline">Pilates and Boxing classes<br>that move your body and soul!</h1>

    <ul class="class-list">
      <li>Pilates mat classes</li>
      <li>Boxing Barre Classes</li>
    </ul>

    <p class="offer">YOUR FIRST CLASS IS FREE!</p>

    <div class="booking-band">
      <svg width="460" height="42" viewBox="0 0 460 42" aria-hidden="true">
        <polygon points="0,0 440,0 460,42 0,42" fill="var(--electric-blue)"/>
      </svg>
      <span>BOOK Online- limited spaces</span>
    </div>

    <address class="contact">
      email: info@thewillowloft.com.au<br>
      <span class="phone">Ph: 0498367205</span>Unit 7 of 12 Pemberly Rd, Ashgrove Vale 2163
    </address>

    <p class="website">www.thewillowloft.com.au</p>
  </main>
</body>
</html>
```